Brontal Land Associates Web Site

We need a website design for a new land purchasing and development business based in PEI. We are just regular guys trying a new adventure buying small parcels of land, doing the hard work seperating them into lots, building roads and selling off a dream location. We help folks like ourselves buy the lots, create a house plan and help get the project done.

We have a wordpress website, but no skills. The site should have our simple story and links to individual land development progects, currently we have 2. The larger project is on a golf course and images have been uploaded. We would like a map of the properities with locations on the properties you can click to see the views/ pictures. It would be great to have the ability to superimpose house images on the lot images. This would help prospects see the end results. I have attached some photos and logo's, however, they are not manditory.
The project would have to allow for us to update and maintain the site.

Target Market(s)

Visitors to PEI, typically from larger cities in Ontario and Maine. Golfers that want to live on a golf course.

Industry/Entity Type

Realestate (land development)

Coding

Coded - Design and coding required

Number of Pages Required

4 page

Requirements
Must have
• Allow fo us to maintain the site. Company overview page with story and contact information. Links to current realestate projects (developments). Project pages with the informaiton on the land and purchasing. Since this is land not houses, maps to the site, maps of the parcel, maps of the individual lots with the ability to review photos based on the views of that particular lot.
Nice to have
• The ability to upload and overlay a house picture on the lot. This would provide a visual of the final build.

```html
<!DOCTYPE html>
<html lang="en">
<head>
<meta charset="utf-8">
<title>Brontal Land Associates</title>
<link href="https://fonts.googleapis.com/css2?family=Poppins:wght@500;600;700&family=Roboto:wght@400;500&display=swap" rel="stylesheet">
<style>
:root{
  --navy:#0b3169;
  --sky:#2ba6df;
  --white:#ffffff;
  --ink:#1b1b1b;
  --footer:#0a2c60;
}
*{margin:0;padding:0;box-sizing:border-box}
html,body{width:1200px;height:3075px;overflow:hidden;background:var(--white)}
body{position:relative;font-family:'Roboto',sans-serif;color:var(--ink)}
.abs{position:absolute}
.brand{display:flex;align-items:center;gap:12px;font-family:'Poppins',sans-serif;font-weight:700;color:var(--navy);font-size:22px;line-height:1.1}
.brand-dot{width:62px;height:62px;border-radius:50%;background:var(--sky);flex:none}
.brand.footer-brand{color:var(--white);font-size:20px}
.brand.footer-brand .brand-dot{background:var(--white);width:50px;height:50px}
.topline{top:18px;display:flex;align-items:center;gap:12px;font-family:'Poppins',sans-serif;font-size:17px;color:var(--sky)}
.ico{width:34px;height:34px;border:2px solid var(--sky);border-radius:50%;display:flex;align-items:center;justify-content:center}
.navband{left:375px;top:65px;width:825px;height:57px;background:var(--navy);clip-path:polygon(0 0,100% 0,100% 100%,25px 100%)}
.nav{top:82px;font-family:'Poppins',sans-serif;font-weight:500;font-size:16px;color:var(--white)}
.nav.active{font-weight:600;font-size:18px;text-decoration:underline;text-underline-offset:5px;top:79px}
.hero{left:0;top:122px;width:1200px;height:600px;background:linear-gradient(180deg,#c9b6ae 0%,#a99b86 15%,#6d6d45 30%,#5a5a30 48%,#7b6a42 62%,#4a4a33 80%,#3a3a2c 100%)}
.hero-shade{left:0;top:122px;width:1200px;height:600px;background:rgba(0,0,0,.18)}
.hero-mark{left:558px;top:186px;width:84px;height:84px;border-radius:50%;background:var(--sky)}
.hero-title{left:0;width:1200px;top:278px;text-align:center;font-family:'Poppins',sans-serif;font-weight:600;font-size:56px;line-height:60px;color:var(--white)}
.hero-text{left:230px;width:740px;top:418px;text-align:center;font-size:16px;line-height:31px;color:var(--white)}
.btn{display:flex;align-items:center;justify-content:center;font-family:'Poppins',sans-serif;font-weight:700;font-size:20px;clip-path:polygon(10px 0,100% 0,calc(100% - 10px) 100%,0 100%)}
.btn-light{background:var(--white);color:var(--navy)}
.btn-dark{background:var(--navy);color:var(--white)}
.h2{font-family:'Poppins',sans-serif;font-weight:700;font-size:34px;color:var(--navy);display:flex;align-items:center;gap:10px}
.h2 .accent{color:var(--sky)}
.h2-dot{width:22px;height:22px;border-radius:50%;background:var(--navy);flex:none}
.h2.light{color:var(--white)}
.h2.light .h2-dot{background:var(--white)}
.about-text{left:110px;top:836px;width:585px;font-size:16px;line-height:31px}
.about-photo{left:740px;top:793px;width:350px;height:350px;border-radius:50%;background:radial-gradient(circle at 50% 30%,#d9e6ef 0%,#9fb28a 35%,#5f7a3c 65%,#3e5426 100%)}
.projects{left:0;top:1228px;width:1200px;height:634px;background:var(--navy)}
.card{width:305px;height:326px}
.arrow{width:34px;height:34px;border-radius:50%;display:flex;align-items:center;justify-content:center}
.overview-text{left:110px;top:1978px;width:980px;text-align:center;font-size:16px;line-height:31px}
.lotmap{left:112px;top:2236px;width:459px;height:454px;background:linear-gradient(135deg,#ececec,#dcdcdc)}
.contact{left:571px;top:2236px;width:517px;height:454px;background:var(--navy)}
.c-item{left:620px;display:flex;gap:38px;align-items:center;color:var(--white)}
.c-ico{width:52px;height:52px;border-radius:50%;background:var(--sky);display:flex;align-items:center;justify-content:center;flex:none}
.c-label{font-family:'Poppins',sans-serif;font-weight:600;font-size:22px}
.c-value{font-family:'Poppins',sans-serif;font-size:16px;margin-top:4px}
.footer{left:0;top:2757px;width:1200px;height:318px;background:var(--footer)}
.fnav{top:2905px;left:0;width:1200px;display:flex;justify-content:center;gap:41px;font-family:'Poppins',sans-serif;font-weight:500;font-size:16px;color:var(--white)}
.social{top:2948px;left:533px;display:flex;gap:13px}
.social span{width:24px;height:24px;border-radius:50%;background:var(--white)}
.copy{top:2998px;left:0;width:1200px;text-align:center;font-family:'Poppins',sans-serif;font-size:16px;color:var(--white)}
</style>
</head>
<body>

<header>
  <div class="abs brand" style="left:108px;top:32px"><span class="brand-dot"></span><span>Brontal Land<br>Associates</span></div>
  <div class="abs topline" style="left:578px">
    <span class="ico"><svg width="16" height="16" viewBox="0 0 24 24"><path fill="#2ba6df" d="M6.6 10.8c1.4 2.8 3.8 5.1 6.6 6.6l2.2-2.2c.3-.3.7-.4 1-.2 1.1.4 2.3.6 3.6.6.6 0 1 .4 1 1V20c0 .6-.4 1-1 1C10.6 21 3 13.4 3 4c0-.6.4-1 1-1h3.5c.6 0 1 .4 1 1 0 1.3.2 2.5.6 3.6.1.3 0 .7-.2 1z"/></svg></span>
    <span>+1 902 555 0147</span>
  </div>
  <div class="abs topline" style="left:808px">
    <span class="ico"><svg width="16" height="16" viewBox="0 0 24 24"><path fill="#2ba6df" d="M3 5h18v14H3z"/><path fill="none" stroke="#fff" stroke-width="2" d="M3 6l9 7 9-7"/></svg></span>
    <span>info@brontalland.com</span>
  </div>
  <div class="abs navband"></div>
  <nav>
    <a class="abs nav active" style="left:491px">Home</a>
    <a class="abs nav" style="left:585px">Company Overview</a>
    <a class="abs nav" style="left:766px">Lot Map</a>
    <a class="abs nav" style="left:864px">Latest &nbsp;Project</a>
    <a class="abs nav" style="left:1010px">Contact Us</a>
  </nav>
</header>

<section>
  <div class="abs hero" role="img" aria-label="Photo of a rural landscape with tall grass and a country road at sunset"></div>
  <div class="abs hero-shade"></div>
  <div class="abs hero-mark"></div>
  <h1 class="abs hero-title">Welcome To Brontal Land And<br>Development Partners</h1>
  <p class="abs hero-text">Lorem Ipsum is simply dummy text of the printing and typesetting industry.It is a long established fact that a reader will be distracted by the readable content of a page when looking at its layout.</p>
  <a class="abs btn btn-light" style="left:480px;top:508px;width:183px;height:47px">Get Started</a>
</section>

<section>
  <h2 class="abs h2" style="left:105px;top:774px"><span class="h2-dot"></span>About <span class="accent">Us</span></h2>
  <p class="abs about-text">Lorem ipsum dolor sit amet, consectetur adipiscing elit, sed do eiusmod tempor incididunt ut labore et dolore magna aliqua. Ut enim ad minim veniam, quis nostrud exercitation ullamco laboris nisi ut aliquip ex ea commodo consequat. Duis aute irure dolor in reprehenderit in voluptate velit esse cillum dolore eu fugiat nulla pariatur. Excepteur sint occaecat cupidatat non proident, sunt in culpa qui officia deserunt mollit anim id est laborum.</p>
  <a class="abs btn btn-dark" style="left:110px;top:1054px;width:166px;height:51px">Read More</a>
  <div class="abs about-photo" role="img" aria-label="Circular photo of a grassy meadow with trees"></div>
</section>

<section>
  <div class="abs projects"></div>
  <h2 class="abs h2 light" style="left:0;width:1200px;justify-content:center;top:1279px">Latest&nbsp; Project</h2>
  <div class="abs arrow" style="left:38px;top:1527px;background:#8a97ad"><svg width="16" height="16" viewBox="0 0 16 16"><path d="M11 2L5 8l6 6" fill="none" stroke="#fff" stroke-width="2"/></svg></div>
  <div class="abs arrow" style="left:1125px;top:1527px;background:var(--white)"><svg width="16" height="16" viewBox="0 0 16 16"><path d="M5 2l6 6-6 6" fill="none" stroke="#111" stroke-width="2"/></svg></div>
  <div class="abs card" style="left:110px;top:1354px;background:linear-gradient(180deg,#dfe6ea 0%,#b7a98a 40%,#5e7a3b 70%,#6b5a42 100%)" role="img" aria-label="Photo of a hand holding a money bag over crop rows"></div>
  <div class="abs card" style="left:447px;top:1399px;background:linear-gradient(180deg,#6e7b86 0%,#8d8a78 30%,#3d4a2a 55%,#2f3a24 100%)" role="img" aria-label="Photo of a country road through a field at dusk"></div>
  <div class="abs" style="left:447px;top:1640px;width:305px;display:flex;justify-content:center;align-items:center;gap:10px;font-family:'Poppins',sans-serif;font-weight:600;font-size:21px;color:#fff">Lorem Ipsum <svg width="22" height="18" viewBox="0 0 22 18"><path d="M1 9h18M12 2l7 7-7 7" fill="none" stroke="#fff" stroke-width="2.5"/></svg></div>
  <div class="abs card" style="left:785px;top:1468px;background:linear-gradient(180deg,#b9c6cf 0%,#7f9a6a 20%,#5ea332 50%,#4b8b26 100%)" role="img" aria-label="Aerial photo of green farmland with a marked parcel boundary"></div>
</section>

<section>
  <h2 class="abs h2" style="left:0;width:1200px;justify-content:center;top:1914px"><span class="h2-dot"></span>Company <span class="accent">Overview</span></h2>
  <p class="abs overview-text">Lorem ipsum dolor sit amet, consectetur adipiscing elit, sed do eiusmod tempor incididunt ut labore et dolore magna aliqua. Ut enim ad minim veniam, quis nostrud exercitation ullamco laboris nisi ut aliquip ex ea commodo consequat. Duis aute irure dolor in reprehenderit in voluptate velit esse cillum dolore eu fugiat nulla pariatur. Excepteur sint occaecat cupidatat non proident, sunt in culpa qui officia deserunt mollit anim id est laborum.</p>
  <a class="abs btn btn-dark" style="left:515px;top:2131px;width:172px;height:49px">Learn More</a>
</section>

<section>
  <div class="abs lotmap" role="img" aria-label="Lot map drawing of the parcel with numbered view points"></div>
  <div class="abs contact"></div>
  <h2 class="abs h2 light" style="left:630px;top:2314px"><span class="h2-dot"></span>Contact Us</h2>
  <div class="abs c-item" style="top:2389px">
    <span class="c-ico"><svg width="22" height="28" viewBox="0 0 22 28"><path d="M11 1C5.5 1 1 5.4 1 10.8 1 18 11 27 11 27s10-9 10-16.2C21 5.4 16.5 1 11 1z" fill="#fff"/><circle cx="11" cy="10.5" r="4" fill="#2ba6df"/></svg></span>
    <div><div class="c-label">Address :</div><div class="c-value">Brontal Land Associates</div></div>
  </div>
  <div class="abs c-item" style="top:2474px">
    <span class="c-ico"><svg width="24" height="24" viewBox="0 0 24 24"><path fill="#fff" d="M6.6 10.8c1.4 2.8 3.8 5.1 6.6 6.6l2.2-2.2c.3-.3.7-.4 1-.2 1.1.4 2.3.6 3.6.6.6 0 1 .4 1 1V20c0 .6-.4 1-1 1C10.6 21 3 13.4 3 4c0-.6.4-1 1-1h3.5c.6 0 1 .4 1 1 0 1.3.2 2.5.6 3.6.1.3 0 .7-.2 1z"/></svg></span>
    <div><div class="c-label">Call :</div><div class="c-value">+1 902 555 0147</div></div>
  </div>
  <div class="abs c-item" style="top:2560px">
    <span class="c-ico"><svg width="22" height="28" viewBox="0 0 22 28"><path d="M11 1C5.5 1 1 5.4 1 10.8 1 18 11 27 11 27s10-9 10-16.2C21 5.4 16.5 1 11 1z" fill="#fff"/><circle cx="11" cy="10.5" r="4" fill="#2ba6df"/></svg></span>
    <div><div class="c-label">Mail :</div><div class="c-value">info@brontallandassociates</div></div>
  </div>
</section>

<footer>
  <div class="abs footer"></div>
  <div class="abs brand footer-brand" style="left:0;width:1200px;justify-content:center;top:2822px"><span class="brand-dot"></span><span>Brontal Land<br>Associates</span></div>
  <nav class="abs fnav"><a>Home</a><a>Company Overview</a><a>Lot Map</a><a>Latest &nbsp;Project</a><a>Contact Us</a></nav>
  <div class="abs social" aria-label="Social links"><span></span><span></span><span></span><span></span></div>
  <p class="abs copy">Copy Rights @ 2022. Brontal Land Associates.All Rights Reserved</p>
</footer>

</body>
</html>
```